Property lawyer needs a website for new law firm Sydney

WHO AM I ?
I am a real estate development lawyer based in suburban Sydney Australia with over 14 years experience and have recently started my own law firm "Tallowbrook Legal". The firm is just me (a female) at this stage. I need a website designed that is capable of being edited by me frequently (hoping this is easily done?!) and can be published with the domain name I own - www.tallowbrooklegal.com.au.
My areas of practice are:
* Property development (strata & community titling, due diligence, easements, by-laws and management statements, structuring etc)
* Conveyancing (sale and purchase of residential, commercial and retail property)
* General property law (caveats, transfers, related party transactions, easements, leases, powers of attorney etc).
WEBSITE REQUIREMENTS
I would like a website which conveys professionalism, has a fresh modern corporate look and is easy to navigate. The website will mostly be accessed by potential clients looking for information about me, my areas of practice and how to get in contact with me. My potential clients are corporate developers and individuals who are buying and selling property.
My logo for Tallowbrook Legal (see attached) is simple, clean and professional looking. I would like the website to work with the logo without being too dark.
I haven't written all of the content yet, so please use filler text for everything and structure the menus as described above. The site will need to be capable of being updated and edited by me.
Other than that I will leave the design up to you.
Thanks and happy designing!
Target Market(s)
Professional developers and individuals buying and selling real estate
Industry/Entity Type
Real Estate
Coding
Coded - Design and coding required
Number of Pages Required
4 page
Requirements
Must have
- I would like a website which conveys professionalism, has a fresh modern corporate look and is easy to navigate. The website will mostly be accessed by potential clients looking for information about me, my areas of practice and how to get in contact with me. My potential clients are corporate developers and individuals who are buying and selling property.
- Please use my logo for Tallowbrook Legal. I would like the website to work with the logo - the colours are a dark blue (C 100% M 50% B 50%) and grey (C10% B 40%). I don't want the website to be too dark though.
- I am thinking 4 pages. I would like links across the top of the page for "Practice Areas", "About us" and "Contact us" - these should lead to separate landing pages with the content to be inserted later.
- The contact page should contain space for a potential client to send an email enquiry to the following email address "enquiries@tallowbrooklegal.com.au". My contact details are set out in the attached letterhead (see attached).
- I would also like the home page to set out what my three Practice Areas are - Property Development; Conveyancing; General Property Law. Each area should have some filler text under it which will be completed later and a link to be able to take me to the "Practice Areas" page where more detail on each will be provided.
- Please select images that are relevant to my practice as a property lawyer. The photos you use will be the ones which I use so please choose wisely.
- I will need a link on the bottom of the home page showing that I am a member of "The Counsel Guild of NSW" (see attached logo).
- The bottom of each page should also include the following statement "Tallowbrook Legal is a business name of Tallowbrook Legal Pty Limited ACN 482 517 306, an incorporated legal practice regulated by the Legal Profession Act 2004. Liability limited by a scheme approved under the Professional Standards Legislation."
Nice to have
- Have attached an image of me (not the best) but at least its me. Consider whether to use on "About us" page
Should not have
- No images of gavels, scales of justice or law books.
- Images not to be too masculine
- Website not to be too dark

```html
<!DOCTYPE html>
<html lang="en">
<head>
<meta charset="utf-8">
<title>Tallowbrook Legal</title>
<link rel="stylesheet" href="https://fonts.googleapis.com/css2?family=Tinos:wght@400;700&family=Source+Sans+3:wght@300;400&display=swap">
<style>
:root{
  --navy:#0d3d73;
  --navy-deep:#0a2f5a;
  --hero-dark:#121416;
  --panel:#f4f5f7;
  --body-text:#8b9097;
  --muted:#a4a8ae;
  --white:#ffffff;
  --line:#c9ccd1;
  --logo-grey:#c7ccd4;
}
*{box-sizing:border-box;margin:0;padding:0}
html,body{width:1200px;height:3586px;overflow:hidden}
body{font-family:"Source Sans 3",Arial,sans-serif;font-weight:300;color:var(--body-text);background:var(--white)}
section,header,footer{position:relative;width:1200px;overflow:visible}
.serif{font-family:Tinos,"Times New Roman",serif}

/* Hero */
.hero{height:605px;background:radial-gradient(ellipse at 70% 60%,#3a3c3f 0%,#1c1e20 45%,var(--hero-dark) 100%)}
.hero-photo{position:absolute;inset:0}
.brand{position:absolute;top:38px;left:0;width:1200px;text-align:center;font-family:Tinos,serif;font-size:80px;letter-spacing:-2px;color:var(--logo-grey);line-height:1;text-transform:uppercase}
.main-nav{position:absolute;top:130px;left:0;width:1200px;display:flex;justify-content:center;gap:58px}
.main-nav a{font-family:Tinos,serif;font-size:14px;color:var(--white);text-decoration:none;letter-spacing:.5px}
.hero-copy{position:absolute;top:236px;left:318px;width:560px}
.hero-copy h1{font-family:Tinos,serif;font-weight:700;font-size:29px;line-height:38px;color:var(--white)}
.hero-copy p{margin-top:14px;font-size:15px;line-height:22px;color:#9da2a8}
.slider-arrows{position:absolute;top:464px;left:529px;display:flex}
.slider-arrows span{width:70px;height:68px;border:1px solid #9a9ea3;display:flex;align-items:center;justify-content:center}
.slider-arrows span+span{border-left:none}

/* Intro */
.intro{height:535px}
.intro h2{position:absolute;top:66px;left:189px;width:822px;font-family:Tinos,serif;font-weight:400;font-size:24px;line-height:31px;color:var(--navy)}
.intro p{position:absolute;left:189px;width:822px;font-size:13.5px;line-height:21px}
.signature{position:absolute;top:450px;left:764px;width:246px;height:60px;background:linear-gradient(90deg,#eceef1,#f6f7f8)}

/* Section titles */
.section-title{position:absolute;left:0;width:1200px;text-align:center;font-family:Tinos,serif;font-weight:400;font-size:35px;color:var(--navy);letter-spacing:.5px}
.title-rule{position:absolute;left:570px;width:60px;height:2px;background:var(--navy)}
.services-head{height:335px}
.services-head .lead{position:absolute;top:186px;left:0;width:1200px;text-align:center;font-family:Tinos,serif;font-size:23px;line-height:31px;color:var(--navy)}
.services-head .sub{position:absolute;top:260px;left:0;width:1200px;text-align:center;font-size:15px;color:var(--muted)}

/* Practice grid */
.practice-grid{height:666px;display:grid;grid-template-columns:600px 600px;grid-template-rows:222px 222px 222px}
.photo{width:100%;height:100%}
.photo-hands{background:linear-gradient(135deg,#6f9cc4,#a9c6dd 55%,#d8b8a4)}
.photo-handshake{background:linear-gradient(120deg,#3b3f47,#c9bfa8 45%,#e07a8c 70%,#a9b8c8)}
.photo-signing{background:linear-gradient(135deg,#2f2f33,#8c8c90 45%,#e3e3e5)}
.practice{padding:34px 0 0 36px}
.practice.light{background:var(--panel)}
.practice.dark{background:var(--navy);padding-left:188px}
.practice h3{font-family:Tinos,serif;font-weight:400;font-size:22px;color:var(--navy)}
.practice.dark h3{color:var(--white)}
.practice p{margin-top:14px;width:420px;font-size:14.5px;line-height:21px;color:var(--muted)}
.practice.dark p{color:#d5dde8;width:380px}
.btn-outline{display:inline-block;margin-top:22px;width:174px;height:40px;line-height:38px;text-align:center;border:1px solid #b7bbc1;font-size:11px;letter-spacing:1px;color:var(--muted);text-transform:uppercase;text-decoration:none}
.practice.dark .btn-outline{border-color:#c9d3e0;color:#dfe6ef}

/* About */
.about-head{height:213px}
.about{height:378px;background:var(--panel)}
.portrait{position:absolute;top:-24px;left:186px;width:268px;height:402px;background:linear-gradient(180deg,#e9e6e2 0%,#8c7f74 18%,#2c2c30 40%,#1f1f22 100%);border-radius:120px 120px 0 0}
.about-copy{position:absolute;top:52px;left:497px;width:516px}
.about-copy p{font-size:13.5px;line-height:21px}
.about-copy p+p{margin-top:20px}
.about-copy h4{margin-top:26px;font-family:Tinos,serif;font-weight:400;font-size:22px;color:var(--navy)}
.about-copy .role{margin-top:6px;font-size:11.5px;line-height:16px;color:#5b6068}

/* Contact */
.contact-head{height:208px}
.contact{height:382px;display:flex}
.map{position:relative;width:600px;height:382px;background:linear-gradient(135deg,#e6e4dc,#d9e3cf 40%,#ece9e2 70%,#dfe6ea)}
.map-card{position:absolute;top:124px;left:175px;width:255px;height:115px;background:var(--white);padding:12px 18px}
.map-card .card-brand{font-family:Tinos,serif;font-size:19px;color:var(--navy);text-transform:uppercase;letter-spacing:-.5px}
.map-card ul{list-style:none;margin-top:6px}
.map-card li{display:flex;align-items:center;gap:8px;font-size:10px;line-height:17px;color:#555a61}
.enquiry{width:600px;background:var(--navy);padding:47px 0 0 43px}
.field{display:flex;width:370px;height:43px;margin-bottom:8px;background:var(--white)}
.field .icon{width:43px;background:#8793a3;display:flex;align-items:center;justify-content:center}
.field span.ph{padding-left:14px;line-height:43px;font-size:10.5px;letter-spacing:.5px;color:#a6abb2;text-transform:uppercase}
.field.tall{height:82px}
.field.tall .icon{align-items:flex-start;padding-top:13px}
.field.tall span.ph{line-height:36px}
.send{margin-top:2px;width:370px;height:40px;border:1px solid #9fb3cc;text-align:center;line-height:38px;font-size:11px;color:var(--white);letter-spacing:1px;text-transform:uppercase}

/* Newsletter */
.newsletter{height:220px;background:var(--panel)}
.newsletter h5{position:absolute;top:48px;left:0;width:1200px;text-align:center;font-family:Tinos,serif;font-weight:700;font-size:14px;color:var(--navy);letter-spacing:.5px}
.subscribe{position:absolute;top:81px;left:428px;display:flex}
.subscribe .email{width:220px;height:37px;background:var(--white);border:1px solid #e1e3e6;font-size:10px;line-height:35px;padding-left:10px;color:#a6abb2;text-transform:uppercase}
.subscribe .go{width:122px;height:37px;background:var(--navy);color:var(--white);font-size:11px;line-height:37px;text-align:center;text-transform:uppercase;margin-left:2px}
.social{position:absolute;top:143px;left:541px;display:flex;gap:10px}
.social span{width:33px;height:33px;border-radius:50%;background:#9fa3a8}

/* Footer */
.site-footer{height:44px;background:var(--navy-deep);text-align:center;line-height:44px;font-size:11px;color:#c7d2e0}
</style>
</head>
<body>

<header class="hero">
  <div class="hero-photo" role="img" aria-label="Dark toned photograph of a lawyer's desk with hands signing documents"></div>
  <div class="brand">Tallowbrook Legal</div>
  <nav class="main-nav">
    <a href="#">HOME</a>
    <a href="#">WHAT WE DO</a>
    <a href="#">WHO WE ARE</a>
    <a href="#">CONTACT US</a>
  </nav>
  <div class="hero-copy">
    <h1>We’re the real estate development lawyer based in suburban Sydney Australia.</h1>
    <p>Our core sectors of expertise are Property development, Conveyancing, General property law.</p>
  </div>
  <div class="slider-arrows">
    <span><svg width="16" height="22" viewBox="0 0 16 22"><path d="M12 3 L4 11 L12 19" fill="none" stroke="#fff" stroke-width="3"/></svg></span>
    <span><svg width="16" height="22" viewBox="0 0 16 22"><path d="M4 3 L12 11 L4 19" fill="none" stroke="#fff" stroke-width="3"/></svg></span>
  </div>
</header>

<section class="intro">
  <h2>Lorem ipsum dolor sit amet, consectetur adipiscing elit. Nunc quis pellentesque justo. Ut at nisi ac lacus rhoncus egestas vitae in sem.</h2>
  <p style="top:148px">Phasellus eu dictum odio. Sed pharetra, libero ac egestas bibendum, magna tortor cursus felis, sed efficitur ipsum lorem at turpis. Vivamus pellentesque vitae lectus ac tempor. Nulla eleifend ligula vitae ligula suscipit, a maximus nisl mattis.</p>
  <p style="top:226px">Donec interdum, metus a venenatis euismod, orci enim viverra libero, vitae molestie lorem justo vel tortor. Sed eu porttitor nisl. Maecenas vestibulum lorem id magna elementum vulputate. Cras placerat, tortor tincidunt rhoncus tincidunt, nisi purus hendrerit justo, eget tempus orci felis nec odio. Curabitur in eros venenatis, sagittis neque eget, ullamcorper ante. Duis viverra purus nec dictum molestie. Cras fringilla a enim vel tempus.</p>
  <p style="top:333px">Donec interdum, metus a venenatis euismod, orci enim viverra libero, vitae molestie lorem justo vel tortor. Sed eu porttitor nisl. Maecenas vestibulum lorem id magna elementum vulputate. Cras placerat, tortor tincidunt rhoncus tincidunt, nisi purus hendrerit justo, eget tempus orci felis nec odio. Curabitur in eros venenatis, sagittis neque eget, ullamcorper ante. Duis viverra purus nec dictum molestie. Cras fringilla a enim vel tempus.</p>
  <div class="signature" role="img" aria-label="Handwritten signature"></div>
</section>

<section class="services-head">
  <h2 class="section-title" style="top:82px">WHAT WE DO</h2>
  <div class="title-rule" style="top:143px"></div>
  <p class="lead">We’re the real estate development lawyer based in Suburban<br>Sydney Australia.</p>
  <p class="sub">Our practice areas include:</p>
</section>

<section class="practice-grid">
  <div class="photo photo-hands" role="img" aria-label="Photograph of cupped hands holding a small house outline"></div>
  <div class="practice light">
    <h3>Property Development</h3>
    <p>Strata &amp; Community Titling, Due Diligence, Easements, By Laws and Management Statements, Structuring etc</p>
    <a class="btn-outline" href="#">Learn more</a>
  </div>
  <div class="practice dark">
    <h3>Conveyancing</h3>
    <p>Sale and Purchase of Residential, Commercial and Retail Property.</p>
    <a class="btn-outline" href="#">Learn more</a>
  </div>
  <div class="photo photo-handshake" role="img" aria-label="Photograph of an agent shaking hands with a couple outside a home"></div>
  <div class="photo photo-signing" role="img" aria-label="Photograph of a hand stamping and signing a contract on a desk"></div>
  <div class="practice light">
    <h3>General Property Law</h3>
    <p>Caveats, Transfers, Related Party Transactions, Easements, Leases, Powers of Attorney etc.</p>
    <a class="btn-outline" href="#">Learn more</a>
  </div>
</section>

<section class="about-head">
  <h2 class="section-title" style="top:90px">WHO WE ARE</h2>
  <div class="title-rule" style="top:151px"></div>
</section>

<section class="about">
  <div class="portrait" role="img" aria-label="Portrait photograph of the principal lawyer in a dark suit"></div>
  <div class="about-copy">
    <p>Donec interdum, metus a venenatis euismod, orci enim viverra libero, vitae molestie lorem justo vel tortor. Sed eu porttitor nisl. Maecenas vestibulum lorem id magna elementum vulputate. Cras placerat, tortor tincidunt rhoncus tincidunt, nisi purus hendrerit justo, eget tempus orci felis nec odio. Curabitur in eros venenatis, sagittis neque eget, ullamcorper ante. Duis viverra purus nec dictum molestie. Cras fringilla a enim vel tempus.</p>
    <p>Phasellus eu dictum odio. Sed pharetra, libero ac egestas bibendum, magna tortor cursus felis, sed efficitur ipsum lorem at turpis.</p>
    <h4>Morgan Ellery</h4>
    <p class="role">Real Estate Lawyer<br>BSc, LLB, LLM (Cant.), GDIP App Law</p>
  </div>
</section>

<section class="contact-head">
  <h2 class="section-title" style="top:90px">GET IN TOUCH</h2>
  <div class="title-rule" style="top:151px"></div>
</section>

<section class="contact">
  <div class="map" role="img" aria-label="Street map of suburban Sydney showing the office location">
    <svg style="position:absolute;top:98px;left:290px" width="20" height="26" viewBox="0 0 20 26"><path d="M10 1a8 8 0 0 0-8 8c0 6 8 16 8 16s8-10 8-16a8 8 0 0 0-8-8z" fill="#d9463b"/><circle cx="10" cy="9" r="3" fill="#fff"/></svg>
    <div class="map-card">
      <div class="card-brand">Tallowbrook Legal</div>
      <ul>
        <li><svg width="9" height="11" viewBox="0 0 20 26"><path d="M10 1a8 8 0 0 0-8 8c0 6 8 16 8 16s8-10 8-16a8 8 0 0 0-8-8z" fill="#0d3d73"/></svg>12 Ridge Lane, Castle Vale, Sydney, Australia</li>
        <li><svg width="10" height="8" viewBox="0 0 20 14"><rect width="20" height="14" fill="#0d3d73"/><path d="M0 0 L10 8 L20 0" fill="none" stroke="#fff" stroke-width="2"/></svg>info@tallowbrooklegal.com.au</li>
        <li><svg width="10" height="10" viewBox="0 0 20 20"><path d="M4 1 L8 5 L6 8 Q9 12 12 14 L15 12 L19 16 L16 19 Q8 18 1 5 Z" fill="#0d3d73"/></svg>02 9000 4417</li>
      </ul>
    </div>
  </div>
  <form class="enquiry">
    <div class="field"><div class="icon"><svg width="16" height="16" viewBox="0 0 16 16"><circle cx="8" cy="5" r="4" fill="#fff"/><path d="M0 16 Q8 6 16 16 Z" fill="#fff"/></svg></div><span class="ph">Your name (required)</span></div>
    <div class="field"><div class="icon"><svg width="16" height="12" viewBox="0 0 16 12"><rect width="16" height="12" fill="#fff"/><path d="M0 0 L8 7 L16 0" fill="none" stroke="#8793a3" stroke-width="1.5"/></svg></div><span class="ph">Your email (required)</span></div>
    <div class="field"><div class="icon"><svg width="16" height="16" viewBox="0 0 20 20"><path d="M4 1 L8 5 L6 8 Q9 12 12 14 L15 12 L19 16 L16 19 Q8 18 1 5 Z" fill="#fff"/></svg></div><span class="ph">Phone number</span></div>
    <div class="field tall"><div class="icon"><svg width="16" height="16" viewBox="0 0 16 16"><path d="M12 1 L15 4 L5 14 L1 15 L2 11 Z" fill="#fff"/></svg></div><span class="ph">Your message</span></div>
    <div class="send">Send now!</div>
  </form>
</section>

<section class="newsletter">
  <h5>SUBSCRIBE OUR NEWSLETTER</h5>
  <div class="subscribe">
    <div class="email">Enter your email</div>
    <div class="go">Send now!</div>
  </div>
  <div class="social"><span></span><span></span><span></span></div>
</section>

<footer class="site-footer">Copyright 2015 TALLOWBROOK LEGAL. All Rights Reserved.</footer>

</body>
</html>
```